Business Card design for construction company

I would like a business card design for a construction company - Harlow Constructions. I have attached the ai logo file for use. I would like the card to be very smart and clean and incorporate only white and the two colours in the logo. I would like the card to have two sides. One side can just have the logo, the other with the relevant information.

Target Market(s)

Building and Construction Clients

Industry/Entity Type

Business

Contact Information for Business Card

Name: Tom Pardoe
Company: Harlow Constructions Pty Limited
Address: 14 Mallee Crescent Carrow Vale 2093
Phone: 0427 531 068
Email: tomp@harlowbuild-example.com.au

Font styles to use
Serif
Sans Serif

Requirements
Must have
• Details noted above
• Logo as provided
• Colours as in logo
• Square edges
• A font that compliments the logo
Should not have
• Any colour other than white and those in logo
• Rounded edges

```html
<!DOCTYPE html>
<html lang="en">
<head>
<meta charset="utf-8">
<title>Harlow Constructions – Business Card</title>
<link rel="stylesheet" href="https://fonts.googleapis.com/css2?family=Aldrich&display=swap">
<style>
  :root {
    --backdrop: #2e3a43;
    --card-white: #ffffff;
    --brand-blue: #1b9fe2;
    --brand-grey: #4b4d50;
    --text-grey: #3f4144;
  }
  * { box-sizing: border-box; margin: 0; padding: 0; }
  html, body {
    width: 1200px;
    height: 1200px;
    overflow: hidden;
    background: var(--backdrop);
    font-family: "Aldrich", "Arial", sans-serif;
  }
  .canvas {
    width: 1200px;
    height: 1200px;
    display: flex;
    flex-direction: column;
    align-items: center;
    justify-content: center;
    gap: 60px;
  }
  .card {
    position: relative;
    width: 760px;
    height: 465px;
    background: var(--card-white);
    display: flex;
    flex-direction: column;
  }
  .wordmark {
    display: flex;
    align-items: center;
    justify-content: center;
    gap: 18px;
    color: var(--brand-grey);
    font-size: 34px;
    letter-spacing: 4px;
    text-transform: uppercase;
  }
  .wordmark-square {
    width: 14px;
    height: 14px;
    background: var(--brand-blue);
  }
  .card-body {
    flex: 1;
    display: flex;
    flex-direction: column;
    align-items: center;
  }
  .card--front .card-body { justify-content: center; padding-bottom: 20px; }
  .card--back .card-body { padding-top: 62px; }
  .contact {
    margin-top: 58px;
    text-align: center;
    color: var(--text-grey);
  }
  .contact-name {
    color: var(--brand-blue);
    font-size: 36px;
    margin-bottom: 8px;
  }
  .contact-email { font-size: 21px; }
  .contact-address { font-size: 23px; margin-top: 42px; }
  .contact-phone { font-size: 23px; margin-top: 6px; }
  .card-band {
    height: 62px;
    background: var(--brand-blue);
    color: var(--card-white);
    display: flex;
    align-items: center;
    justify-content: center;
  }
  .band-web { font-size: 21px; letter-spacing: 1px; }
  .band-company {
    font-size: 22px;
    letter-spacing: 9px;
    text-transform: uppercase;
  }
</style>
</head>
<body>
<main class="canvas">
  <section class="card card--front" aria-label="Card front">
    <div class="card-body">
      <div class="wordmark">
        <span class="wordmark-square" aria-hidden="true"></span>
        <span class="wordmark-name">Harlow Constructions</span>
      </div>
    </div>
    <div class="card-band"><span class="band-web">www.harlowbuild-example.com.au</span></div>
  </section>

  <section class="card card--back" aria-label="Card back">
    <div class="card-body">
      <div class="wordmark">
        <span class="wordmark-square" aria-hidden="true"></span>
        <span class="wordmark-name">Harlow Constructions</span>
      </div>
      <div class="contact">
        <p class="contact-name">Tom Pardoe</p>
        <p class="contact-email">tomp@harlowbuild-example.com.au</p>
        <p class="contact-address">14 Mallee Crescent Carrow Vale 2093</p>
        <p class="contact-phone">0427 531 068</p>
      </div>
    </div>
    <div class="card-band"><span class="band-company">Harlow Constructions Pty Limited</span></div>
  </section>
</main>
</body>
</html>
```